Oil and Gas Industry training School Needs a Web Design

We need a web design for a new company based in Northern British Columbia Canada called "SKILLPATH Trade Academy Inc." Is a training facility that specializes in different aspects of Pipeline Construction training. We also offer compliance courses for Oil and Gas Industry. We would like to see designs that us the colours in our logo.

Target Market(s)

Is Men and women between 18-60 that want to work in the oil and gas industry

Industry/Entity Type

School

Number of Pages Required

5+ page

Font styles to use
Sans Serif

Colors
f37022
000000
333333
ffffff
848484
7f7f7f
c8c8c8
f68d4d
fee3d4

Requirements
Must have
• a easy back end for editing content! and adding additional pages if necessary.

```html
<!DOCTYPE html>
<html lang="en">
<head>
<meta charset="utf-8">
<title>SKILLPATH Trade Academy Inc.</title>
<link href="https://fonts.googleapis.com/css2?family=Rubik:wght@400;500;700&display=swap" rel="stylesheet">
<style>
:root{
  --orange:#f37022;
  --orange-soft:#f68d4d;
  --orange-pale:#fee3d4;
  --black:#000000;
  --ink:#333333;
  --dark:#222222;
  --grey:#848484;
  --grey-2:#7f7f7f;
  --grey-light:#c8c8c8;
  --white:#ffffff;
}
*{box-sizing:border-box;margin:0;padding:0}
html,body{width:722px;height:1200px;overflow:hidden;background:var(--white)}
body{font-family:"Rubik",Arial,sans-serif;color:var(--ink);position:relative}
.site{position:relative;width:722px;height:1200px}
a{text-decoration:none}

/* header */
.site-header{position:absolute;top:0;left:0;width:722px;height:38px;background:var(--white);display:flex;align-items:center;justify-content:space-between;padding:0 30px 0 18px;z-index:5}
.brand{display:flex;align-items:center;gap:6px}
.brand-dot{width:22px;height:22px;border-radius:50%;background:var(--ink)}
.brand-name{font-size:11px;font-weight:500;color:var(--ink);line-height:1}
.main-nav{display:flex;gap:22px}
.main-nav a{font-size:7px;font-weight:500;color:var(--ink)}

/* hero */
.hero{position:absolute;top:38px;left:0;width:722px;height:275px;overflow:hidden}
.hero-photo{position:absolute;inset:0;background:linear-gradient(180deg,#cfcfcf 0%,#bdbdbd 55%,#a9a9a9 100%)}
.hero-title{position:absolute;top:88px;width:100%;text-align:center;font-size:27px;font-weight:700;color:var(--black);letter-spacing:-.2px}
.hero-title span{color:#4a4a4a}
.hero-sub{position:absolute;top:128px;width:100%;text-align:center;font-size:10px;font-weight:500;color:var(--ink)}
.btn{display:inline-flex;flex-direction:column;align-items:center;justify-content:center;background:var(--orange);color:var(--white);font-weight:500}
.hero-btn{position:absolute;left:305px;top:157px;width:112px;height:28px;font-size:11px;flex-direction:row;gap:4px}
.menu-ico{width:10px;height:8px}

/* training */
.training{position:absolute;top:313px;left:0;width:722px;height:290px;background:var(--dark);overflow:hidden}
.section-title{font-size:19px;font-weight:500;text-align:center}
.training .section-title{position:absolute;top:20px;width:100%;color:var(--white)}
.title-rule{position:absolute;top:49px;left:348px;width:26px;height:2px;background:var(--orange)}
.photo-frame{position:absolute;left:108px;top:80px;width:188px;height:122px}
.photo-back{position:absolute;left:2px;top:6px;width:180px;height:110px;background:var(--orange);transform:rotate(-7deg)}
.photo{position:absolute;left:10px;top:2px;width:177px;height:118px;background:linear-gradient(135deg,#8a6f52,#b98459 45%,#6b8199);border:2px solid var(--white)}
.training-copy{position:absolute;left:317px;top:80px;width:280px;font-size:6.6px;line-height:8.2px;font-weight:500;color:var(--white)}
.training-copy p+p{margin-top:8px}
.catalogue-btn{position:absolute;left:361px;top:235px;width:184px;height:31px}
.catalogue-btn strong{font-size:10.5px;font-weight:500}
.catalogue-btn small{font-size:5px;font-weight:700;margin-top:1px}

/* courses */
.courses{position:absolute;top:603px;left:0;width:722px;height:258px;background:var(--white)}
.courses .section-title{position:absolute;top:27px;width:100%;color:var(--orange);font-weight:700}
.courses-intro{position:absolute;top:68px;left:82px;width:558px;text-align:center;font-size:6.4px;line-height:10.4px;font-weight:500;color:var(--ink)}
.course-link{position:absolute;top:168px;width:130px;text-align:center;text-decoration:none}
.course-link svg{display:block;margin:0 auto 10px}
.course-link span{font-size:10.5px;font-weight:500;color:var(--ink)}

/* testimonials */
.testimonials{position:absolute;top:861px;left:0;width:722px;height:203px;overflow:hidden}
.testimonials-photo{position:absolute;inset:0;background:radial-gradient(ellipse at 48% 45%,#e07a3c 0%,#ea7536 40%,#e9702e 100%)}
.testimonials .section-title{position:absolute;top:25px;width:100%;color:var(--white)}
.quote{position:absolute;top:70px;width:239px}
.quote-box{position:relative;height:63px;padding:11px 14px;background:rgba(255,255,255,.18);border-radius:3px;font-size:6.8px;line-height:10.5px;font-weight:500;color:var(--white)}
.quote-box::after{content:"";position:absolute;left:30px;bottom:-6px;border:6px solid transparent;border-bottom:0;border-top-color:rgba(255,255,255,.18)}
.author{display:flex;align-items:center;gap:6px;margin-top:16px;padding-left:15px}
.avatar{width:32px;height:32px;border-radius:50%;background:#d9b79f;border:2px solid var(--white)}
.author-name{font-size:9px;font-weight:500;color:var(--white)}

/* footer */
.site-footer{position:absolute;top:1064px;left:0;width:722px;height:136px;background:var(--dark)}
.follow{position:absolute;top:9px;width:100%;text-align:center;font-size:6.5px;font-weight:700;letter-spacing:.6px;color:var(--white)}
.social{position:absolute;top:21px;left:331px;display:flex;gap:5px}
.social a{width:16px;height:16px;border-radius:50%;display:block}
.social .s1{background:#3b67b3}.social .s2{background:#2fa9e0}.social .s3{background:#dd4b39}
.newsletter{position:absolute;top:50px;left:185px;width:347px;height:30px;background:#f4f4f4;border-radius:2px;display:flex;align-items:center;justify-content:space-between;padding:0 16px 0 9px}
.newsletter span{font-size:7.5px;color:#a8a8a8}
.footer-nav{position:absolute;top:97px;left:108px;display:flex;gap:21px}
.footer-nav a{font-size:6.8px;font-weight:500;color:var(--white)}
.copyright{position:absolute;top:112px;left:108px;font-size:6.3px;font-weight:500;color:var(--orange)}
.footer-brand{position:absolute;top:98px;left:508px;display:flex;align-items:center;gap:6px}
.footer-brand .brand-dot{width:16px;height:16px;background:var(--grey-2)}
.footer-brand .brand-name{font-size:10px;color:var(--grey-2)}
</style>
</head>
<body>
<div class="site">

  <header class="site-header">
    <div class="brand"><span class="brand-dot"></span><span class="brand-name">SKILLPATH</span></div>
    <nav class="main-nav">
      <a href="#">Home</a><a href="#">About Us</a><a href="#">Training</a><a href="#">Compliance Courses</a><a href="#">Contact Us</a>
    </nav>
  </header>

  <section class="hero">
    <div class="hero-photo" role="img" aria-label="Faded grey photo of pipeline construction equipment and pipework"></div>
    <h1 class="hero-title">SKILLPATH <span>Trade Academy Inc</span></h1>
    <p class="hero-sub">is committed to providing awareness for new and seasoned people in the pipeline construction industry</p>
    <a class="btn hero-btn" href="#">
      <svg class="menu-ico" viewBox="0 0 10 8"><rect width="10" height="1.6" fill="#fff"/><rect y="3.2" width="10" height="1.6" fill="#fff"/><rect y="6.4" width="10" height="1.6" fill="#fff"/></svg>
      Read More
    </a>
  </section>

  <section class="training">
    <h2 class="section-title">Pipeline Construction Safety Training</h2>
    <div class="title-rule"></div>
    <div class="photo-frame">
      <div class="photo-back"></div>
      <div class="photo" role="img" aria-label="Photo of two workers in safety vests beside a pipeline welding truck"></div>
    </div>
    <div class="training-copy">
      <p>Lorem ipsum dolor sit amet, consectetur adipiscing elit. Proin quis tortor tincidunt lectus tincidunt dapibus. Sed rutrum neque id cursus bibendum. Phasellus sit amet purus massa. Aliquam erat volutpat. Nullam ut dignissim ligula. In posuere felis sit amet accumsan faucibus. Phasellus consequat quam eget orci commodo, a venenatis nunc lacinia. Pellentesque tincidunt ligula non dolor tristique, sed sagittis neque rhoncus. Curabitur feugiat placerat est, eu suscipit tellus viverra ac.</p>
      <p>Nunc mollis est a ultricies ullamcorper. Donec suscipit blandit consectetur. Nam in urna vel leo euismod ultricies non ut nunc. Donec dignissim bibendum ex. Maecenas vel eros dolor.</p>
      <p>Sed a dictum est. Pellentesque eleifend eleifend ex ac eleifend. Nam in nulla mi. Proin justo diam, pellentesque non orci id, egestas auctor tellus. Aliquam vitae libero ac turpis elementum ultrices. Aenean fringilla lacus at felis bibendum, eu malesuada dui placerat.</p>
    </div>
    <a class="btn catalogue-btn" href="#"><strong>Download Training Catalogue</strong><small>Available Latest Version 3.4.12 &nbsp;-&nbsp; Price: $30</small></a>
  </section>

  <section class="courses">
    <h2 class="section-title">Compliance e-Courses</h2>
    <p class="courses-intro">e-Learning programs, Web-based (Online) or Computer based (CDROM), provide an excellent training alternative to the classroom. e-Learning programs use video, audio, text and are adaptable to each learner's preference of information gathering and speed of comprehension. e-Learning also allows greater mobility of training, removing the barriers of time and location, and are virtually irreplacable in conducting objective testing.</p>

    <a class="course-link" href="#" style="left:130px">
      <svg width="30" height="36" viewBox="0 0 30 36" fill="none" stroke="#f37022" stroke-width="1.6">
        <rect x="5" y="4" width="22" height="30"/><path d="M2 1h20v3M2 1v30h3"/>
        <rect x="9" y="11" width="8" height="7" fill="#f37022"/><path d="M19 12h5M19 16h5M9 22h15M9 26h15M9 30h10"/>
      </svg>
      <span>Course Content</span>
    </a>
    <a class="course-link" href="#" style="left:293px">
      <svg width="30" height="36" viewBox="0 0 30 36" fill="none" stroke="#f37022" stroke-width="1.8">
        <rect x="4" y="2" width="23" height="32" rx="2"/><path d="M9 2v32M16 2v13l3-3 3 3V2"/><path d="M2 8h4M2 14h4M2 20h4M2 26h4"/>
      </svg>
      <span>Download Brochure</span>
    </a>
    <a class="course-link" href="#" style="left:464px">
      <svg width="30" height="36" viewBox="0 0 30 36" fill="none" stroke="#f37022" stroke-width="1.8">
        <path d="M4 20a8 8 0 0 1 16 0v6a8 8 0 0 1-16 0z"/><path d="M4 22h16M12 12v10"/>
        <path d="M12 12c0-4 2-5 4-5s3 3 5 3 3-2 4-3" stroke-linecap="round"/>
      </svg>
      <span>Apply Now!!!</span>
    </a>
  </section>

  <section class="testimonials">
    <div class="testimonials-photo" role="img" aria-label="Orange-tinted photo of a pipeline worker inside a large pipe"></div>
    <h2 class="section-title">What people are saying about us</h2>
    <div class="quote" style="left:108px">
      <p class="quote-box">Lorem ipsum dolor sit amet, consectetur adipiscing elit. Morbi dictum orci risus, in tincidunt leo convallis sit amet. Morbi finibus lorem in orci condimentum placerat. Sed at sem lectus.</p>
      <div class="author"><span class="avatar" role="img" aria-label="Portrait of Aaron Kowalski"></span><span class="author-name">Aaron Kowalski</span></div>
    </div>
    <div class="quote" style="left:378px">
      <p class="quote-box">Lorem ipsum dolor sit amet, consectetur adipiscing elit. Morbi dictum orci risus, in tincidunt leo convallis sit amet. Morbi finibus lorem in orci condimentum placerat. Sed at sem lectus.</p>
      <div class="author"><span class="avatar" role="img" aria-label="Portrait of Dylan Okafor"></span><span class="author-name">Dylan Okafor</span></div>
    </div>
  </section>

  <footer class="site-footer">
    <p class="follow">Follow us on</p>
    <div class="social"><a class="s1" href="#" aria-label="Social link 1"></a><a class="s2" href="#" aria-label="Social link 2"></a><a class="s3" href="#" aria-label="Social link 3"></a></div>
    <div class="newsletter">
      <span>Subscribe for our Newsletter</span>
      <svg width="11" height="10" viewBox="0 0 11 10"><path d="M0 5 11 0 8 10 5 6z" fill="#f37022"/></svg>
    </div>
    <nav class="footer-nav">
      <a href="#">Home</a><a href="#">About Us</a><a href="#">Training</a><a href="#">Compliance Courses</a><a href="#">Contact Us</a>
    </nav>
    <p class="copyright">© 2014. SKILLPATH. All rights reserved.</p>
    <div class="footer-brand"><span class="brand-dot"></span><span class="brand-name">SKILLPATH</span></div>
  </footer>

</div>
</body>
</html>
```